Land Buying Company Needs Letterhead for Direct Mail Marketing to Land Owners

We are looking for a professional letterhead that we will be including in our direct mail marketing. We will be sending this to land owners who may be interested in selling or purchasing land.

The letterhead needs to be editable. Headers and footers would look nice, but we are open. We would want it to include our address, website, phone, and email info. For right now the address to use for design purposes would the following:

Address: 415 Bramwell Avenue #600
Dallas, TX 75219
Website - www.quillridgeacres.example
Email - info@quillridgeacres.example
Phone - 866-402-ACRE

I have attached our logo zip file that we just had done on Pixel Guild. Let me know what questions you have, and thank you.

```html
<!DOCTYPE html>
<html lang="en">
<head>
<meta charset="utf-8">
<title>Quill Ridge Acres Letterhead</title>
<link rel="stylesheet" href="https://fonts.googleapis.com/css2?family=Poppins:wght@300;400&family=Montserrat:wght@600&display=swap">
<style>
  :root {
    --backdrop: #e9e9e7;
    --paper: #f6f6f5;
    --forest: #3f5a26;
    --leaf: #7db53c;
    --ink: #4a4a4a;
    --wash: #dedfda;
  }
  * { box-sizing: border-box; margin: 0; padding: 0; }
  html, body {
    width: 1200px; height: 795px; overflow: hidden;
    background: var(--backdrop);
  }
  .letterhead {
    position: absolute;
    left: 314px; top: 27px;
    width: 572px; height: 740px;
    background: var(--paper);
    overflow: hidden;
    box-shadow: 0 2px 8px rgba(0,0,0,0.08);
    font-family: 'Poppins', sans-serif;
    color: var(--ink);
  }
  .header-wash {
    position: absolute;
    left: -150px; top: -40px;
    width: 420px; height: 420px;
    border-radius: 50%;
    background: radial-gradient(circle at 50% 45%, #e2e3de 0%, var(--wash) 70%);
  }
  .brand {
    position: absolute;
    left: 34px; top: 196px;
    display: flex; align-items: center; gap: 10px;
  }
  .brand-dot {
    width: 40px; height: 40px; border-radius: 50%;
    background: var(--forest);
  }
  .brand-name {
    font-family: 'Montserrat', sans-serif;
    font-weight: 600;
    font-size: 19px;
    letter-spacing: 1.5px;
    line-height: 1.1;
    color: var(--leaf);
    text-transform: uppercase;
  }
  .contact {
    position: absolute;
    right: 32px; top: 30px;
    text-align: right;
    font-size: 8.5px;
    line-height: 1.45;
    font-weight: 300;
  }
  .contact-rule {
    height: 1px; width: 140px;
    background: var(--leaf);
    margin: 4px 0 4px auto;
  }
  .contact-row {
    display: flex; justify-content: flex-end; align-items: center; gap: 5px;
  }
  .contact-icon {
    width: 8px; height: 8px; border-radius: 50%;
    background: var(--forest);
    flex: none;
  }
  .footer {
    position: absolute;
    left: 0; right: 0; bottom: 14px;
    display: flex; align-items: center; gap: 6px;
    padding-left: 0; padding-right: 0;
  }
  .footer-line {
    height: 1px; background: var(--leaf);
  }
  .footer-line.long { flex: 1; }
  .footer-line.short { width: 24px; }
  .footer-web {
    font-size: 9px; font-weight: 300;
    white-space: nowrap;
  }
  .footer-band {
    position: absolute;
    left: 0; right: 0; bottom: 0;
    height: 9px;
    background: var(--forest);
  }
</style>
</head>
<body>
  <main class="letterhead">
    <div class="header-wash" role="img" aria-label="Faint decorative backdrop of a bird over pine trees"></div>

    <div class="brand">
      <span class="brand-dot"></span>
      <span class="brand-name">Quill Ridge Acres</span>
    </div>

    <address class="contact" style="font-style:normal">
      <div>415 Bramwell Avenue #600</div>
      <div>Dallas, TX 75219</div>
      <div class="contact-rule"></div>
      <div class="contact-row"><span>866-402-ACRE</span><span class="contact-icon"></span></div>
      <div class="contact-row"><span>info@quillridgeacres.example</span><span class="contact-icon"></span></div>
    </address>

    <footer class="footer">
      <span class="footer-line long"></span>
      <span class="footer-web">www.quillridgeacres.example</span>
      <span class="footer-line short"></span>
    </footer>
    <div class="footer-band"></div>
  </main>
</body>
</html>
```